Hopfield Taproom tasting invitation

I require a professionally designed invitation I can use to send to lawyers and bankers to invite them to a beer tasting event.

The invite needs to be able to be sent out in soft copy (PDF) and hard copy print.

Visual queues can be taken from googling "beer tasting invitation" images.

Target Market(s)

Bankers and lawyers who love beer

Industry/Entity Type

Event

Requirements
Nice to have
• A cool Hopfield Taproom feel - http://linkmuddle.net/qpv7tx4

```html
<!DOCTYPE html>
<html lang="en">
<head>
<meta charset="utf-8">
<title>Hopfield Taproom – Restructuring Craft Celebration</title>
<link rel="stylesheet" href="https://fonts.googleapis.com/css2?family=Fondamento:ital@0;1&display=swap">
<style>
  :root {
    --wood-light: #c98a5e;
    --wood-mid: #b3703f;
    --wood-deep: #97552f;
    --roof-dark: #6d2a1a;
    --ink: #1a0f0a;
    --claret: #7c1a12;
    --paper: #ffffff;
    --frame-line: #2b130b;
  }
  html, body {
    margin: 0;
    padding: 0;
    overflow: hidden;
    background: #2a2220;
  }
  .invitation {
    position: relative;
    width: 848px;
    height: 1200px;
    overflow: hidden;
    font-family: "Fondamento", "Palatino Linotype", serif;
  }
  .invitation__art {
    position: absolute;
    inset: 0;
    width: 848px;
    height: 1200px;
    display: block;
  }
  .event-title {
    position: absolute;
    left: 0;
    width: 868px;
    margin: 0;
    text-align: center;
    color: var(--ink);
    font-style: italic;
    font-weight: 400;
    font-size: 66px;
    line-height: 72px;
    letter-spacing: 1px;
    top: 850px;
  }
  .event-date {
    position: absolute;
    left: 0;
    width: 868px;
    margin: 0;
    text-align: center;
    color: var(--claret);
    font-style: italic;
    font-size: 44px;
    line-height: 50px;
    top: 1028px;
  }
  .event-time {
    position: absolute;
    left: 0;
    width: 868px;
    margin: 0;
    text-align: center;
    color: var(--ink);
    font-style: italic;
    font-size: 36px;
    line-height: 42px;
    top: 1082px;
  }
  .host-name {
    font-family: "Fondamento", "Palatino Linotype", serif;
    font-size: 58px;
    fill: var(--claret);
  }
  .welcome {
    font-family: "Fondamento", "Palatino Linotype", serif;
    font-style: italic;
    font-size: 50px;
    letter-spacing: 3px;
    fill: var(--paper);
  }
</style>
</head>
<body>
<main class="invitation">
  <svg class="invitation__art" viewBox="0 0 848 1200" xmlns="http://www.w3.org/2000/svg">
    <defs>
      <linearGradient id="woodTone" x1="0" y1="0" x2="1" y2="1">
        <stop offset="0" stop-color="var(--wood-light)"/>
        <stop offset="0.45" stop-color="var(--wood-mid)"/>
        <stop offset="1" stop-color="var(--wood-deep)"/>
      </linearGradient>
      <radialGradient id="warmGlow" cx="0.72" cy="0.72" r="0.5">
        <stop offset="0" stop-color="#8a3a22" stop-opacity="0.35"/>
        <stop offset="1" stop-color="#8a3a22" stop-opacity="0"/>
      </radialGradient>
      <clipPath id="badgeClip">
        <circle cx="440" cy="399" r="288"/>
      </clipPath>
    </defs>

    <!-- wood board -->
    <rect class="board" width="848" height="1200" fill="url(#woodTone)" role="img" aria-label="Warm brown wood grain texture"/>
    <rect class="board-glow" width="848" height="1200" fill="url(#warmGlow)" role="img" aria-label="Soft sunburst rays in reddish brown"/>

    <!-- darker roof corners -->
    <polygon class="roof-corner" points="0,0 424,0 0,150" fill="var(--roof-dark)" opacity="0.8"/>
    <polygon class="roof-corner" points="424,0 848,0 848,150" fill="var(--roof-dark)" opacity="0.8"/>

    <!-- inner frame -->
    <polyline class="frame" points="71,150 71,1134 778,1134 778,150" fill="none" stroke="var(--frame-line)" stroke-width="1.6"/>

    <!-- white band -->
    <rect class="band" x="0" y="383" width="848" height="75" fill="var(--paper)"/>

    <!-- circular badge -->
    <circle class="badge" cx="440" cy="399" r="288" fill="url(#woodTone)"/>
    <polygon class="badge-notch" clip-path="url(#badgeClip)" points="300,790 300,760 440,718 580,760 580,790" fill="var(--paper)" opacity="0.92"/>
    <circle class="badge-ring" cx="440" cy="399" r="288" fill="none" stroke="var(--paper)" stroke-width="2"/>

    <!-- host name -->
    <text class="host-name" x="440" y="410" text-anchor="middle">Hopfield Taproom</text>

    <!-- arched greeting -->
    <path id="welcomeArc" d="M 120 900 Q 430 640 740 900" fill="none"/>
    <text class="welcome">
      <textPath href="#welcomeArc" startOffset="50%" text-anchor="middle">WELCOME TO ALL</textPath>
    </text>

    <!-- divider -->
    <line class="divider" x1="212" y1="1016" x2="663" y2="1016" stroke="var(--ink)" stroke-width="2"/>
  </svg>

  <h1 class="event-title">Restructuring<br>Craft celebration</h1>
  <p class="event-date">XX August 2016</p>
  <p class="event-time">6.30pm – 9.30 pm</p>
</main>
</body>
</html>
```